Harrowgate Estates Business Card for Apartment Buildings

Create business cards for resident managers who run apartment buildings. The audience is the public who are searching for apartment rentals, and current residents who live at the apartment building. Key design element will be incorporating the company logo, however, the logo cannot dominate. The building name and manager name are more important than the logo. Current business card design leaves little room for copy, so we may need to reduce the size on the current card to allow for more space for copy.

Target Market(s)

Adults 18-65 years of age, who are looking for an apartment rental, plus current residents who live at our apartment buildings.

Industry/Entity Type

Property Management

Contact Information for Business Card

A major design element will be use of the company logo. Important property and manager contact information must be part of the design. The size of the logo will need to be reduced to make room for building and manager contact copy.

Font styles to use
Sans Serif

Colors
3176b5
000000
959595
ffffff

Requirements
Must have
• 1) Incorporate the company logo.
• 2) Use the company colors (dark blue, black/grey, over white).
• 3) FEATURE THE BUILDING NAME
• 4) FEATURE THE MANAGER NAME
• 5) The company name is less important than BUILDING and MANAGER
• 6) Manager contact information
• **SEE ATTACHED CREATIVE BRIEF**
Nice to have
• 1) Back of card logo watermark
• 2) Ability to write notes on back of carfd
Should not have
• Avoid letting the company logo dominate the card, the building name and manager are more important than the company logo.

```html
<!DOCTYPE html>
<html lang="en">
<head>
<meta charset="utf-8">
<title>Harrowgate Estates – Business Card</title>
<link href="https://fonts.googleapis.com/css2?family=Work+Sans:wght@400;500;600;700&display=swap" rel="stylesheet">
<style>
  :root {
    --brand-blue: #3176b5;
    --deep-blue: #1d62a3;
    --ink: #222222;
    --grey: #959595;
    --paper: #ffffff;
    --backdrop: #e6e8eb;
  }
  * { box-sizing: border-box; margin: 0; padding: 0; }
  html, body { width: 1200px; height: 900px; overflow: hidden; }
  body {
    background: var(--backdrop);
    font-family: "Work Sans", Arial, sans-serif;
    position: relative;
  }
  .card {
    position: absolute;
    left: 250px;
    width: 700px;
    height: 400px;
    border-radius: 22px;
    overflow: hidden;
    box-shadow: 0 10px 28px rgba(0,0,0,0.18);
  }
  .card-front { top: 40px; background: linear-gradient(135deg, #f4f5f7 0%, var(--paper) 45%); }
  .card-back { top: 460px; background: var(--brand-blue); }

  .manager-block { position: absolute; left: 48px; top: 44px; }
  .manager-name { color: var(--brand-blue); font-size: 34px; font-weight: 500; line-height: 1.1; }
  .manager-title { color: var(--ink); font-size: 17px; margin-top: 4px; }
  .building-name { color: var(--brand-blue); font-size: 19px; font-weight: 500; margin-top: 22px; }
  .building-address { color: var(--ink); font-size: 17px; line-height: 1.3; margin-top: 2px; }

  .contact-list { list-style: none; margin-top: 20px; }
  .contact-list li {
    display: flex; align-items: center; gap: 12px;
    color: var(--ink); font-size: 16px; line-height: 1.5;
  }
  .contact-list svg { width: 14px; height: 14px; fill: var(--brand-blue); flex: none; }
  .contact-list .web-lead { color: var(--ink); }
  .contact-list .web-domain { color: var(--brand-blue); }

  .company-mark {
    position: absolute; right: 48px; bottom: 40px;
    color: var(--brand-blue); font-weight: 700; text-transform: uppercase;
    text-align: right; line-height: 1;
  }
  .company-mark .mark-main { font-size: 48px; letter-spacing: 1px; display: block; }
  .company-mark .mark-sub { font-size: 20px; letter-spacing: 6px; display: block; margin-top: 8px; }

  .back-pattern {
    position: absolute; inset: 0;
    background: linear-gradient(135deg, #3a80bf 0%, var(--brand-blue) 50%, var(--deep-blue) 100%);
  }
  .back-content {
    position: absolute; inset: 0;
    display: flex; flex-direction: column; align-items: center; justify-content: center;
    color: var(--paper);
  }
  .back-mark { display: flex; align-items: center; gap: 22px; font-weight: 700; text-transform: uppercase; }
  .back-mark .mark-dot { width: 70px; height: 70px; border-radius: 50%; background: var(--paper); flex: none; }
  .back-mark .mark-text { line-height: 1; }
  .back-mark .mark-main { font-size: 56px; letter-spacing: 1px; display: block; }
  .back-mark .mark-sub { font-size: 22px; letter-spacing: 7px; display: block; margin-top: 8px; }
  .back-web { font-size: 20px; margin-top: 44px; letter-spacing: 1px; }
</style>
</head>
<body>
  <section class="card card-front">
    <div class="manager-block">
      <h1 class="manager-name">Marisol Delgado</h1>
      <p class="manager-title">Resident Manager</p>
      <p class="building-name">Linden Court Apartments</p>
      <p class="building-address">4825 Cedar Lane<br>Fairhaven, CA 92480</p>
      <ul class="contact-list">
        <li><svg viewBox="0 0 16 16"><path d="M3 1l3 3-2 2c1 2 4 5 6 6l2-2 3 3-2 2C7 15 1 9 1 3z"/></svg>555-214-3380</li>
        <li><svg viewBox="0 0 16 16"><path d="M4 0h8a1 1 0 0 1 1 1v14a1 1 0 0 1-1 1H4a1 1 0 0 1-1-1V1a1 1 0 0 1 1-1zm1 2v10h6V2zm3 11a1 1 0 1 0 0 2 1 1 0 0 0 0-2z"/></svg>555-867-4120</li>
        <li><svg viewBox="0 0 16 16"><path d="M4 1h7v4H4zM2 6h12a1 1 0 0 1 1 1v6h-3v2H4v-2H1V7a1 1 0 0 1 1-1zm3 5v3h6v-3z"/></svg>555-302-9915</li>
        <li><svg viewBox="0 0 16 16"><path d="M1 3h14v10H1zm1.5 1.2v.3L8 8.6l5.5-4.1v-.3z"/></svg>marisol@harrowgateest.com</li>
        <li><svg viewBox="0 0 16 16"><path d="M8 1a7 7 0 1 0 0 14A7 7 0 0 0 8 1zm0 1.5c.8 0 1.7 1.7 2 4H6c.3-2.3 1.2-4 2-4zM2.6 7.5h2.3c0-1.6.4-3 .9-4a5.6 5.6 0 0 0-3.2 4zm8.5 0h2.3a5.6 5.6 0 0 0-3.2-4c.5 1 .9 2.4.9 4zM6 8.5h4c-.3 2.3-1.2 4-2 4s-1.7-1.7-2-4zm-3.4 0a5.6 5.6 0 0 0 3.2 4c-.5-1-.9-2.4-.9-4zm8.5 0c0 1.6-.4 3-.9 4a5.6 5.6 0 0 0 3.2-4z"/></svg><span><span class="web-lead">www.</span><span class="web-domain">harrowgateest</span><span class="web-lead">.com</span></span></li>
      </ul>
    </div>
    <div class="company-mark">
      <span class="mark-main">Harrowgate</span>
      <span class="mark-sub">Estates LLC</span>
    </div>
  </section>

  <section class="card card-back">
    <div class="back-pattern" role="img" aria-label="Faint repeating company emblem pattern across the blue card back"></div>
    <div class="back-content">
      <div class="back-mark">
        <span class="mark-dot"></span>
        <span class="mark-text">
          <span class="mark-main">Harrowgate</span>
          <span class="mark-sub">Estates LLC</span>
        </span>
      </div>
      <p class="back-web">www.harrowgateest.com</p>
    </div>
  </section>
</body>
</html>
```